Gourmet food company looking for a dazzling label for their premuim vinagrette dressings

Need a food label that will dazzle our customer and prove what a premium product we have. We make high end gourmet dressing for vegetables, fruit, meat, poultry and fish.

Our label will fit on a 250 mil Tolvenna Square bottle. Labels should be a 4x5 or even 5x5 depending on the design. Nutritionals, bar codes and company blurb will be supplied later. We really want to test you all's talent on this one and are very excited to see your renderings!

Our dressings are Champagne Pear Vinaigrette, White Balsmic Vinaigrette, Mojito Lime Vinaigrette, Creamy-Avacado Lime Vinaigrette, and Asian Sesame Vinaigrette. I hope these names will help you envision our product and kinda what we are looking for.

Thank you all so far for your renderings.I really don't want pictures if that helps. Our logo can be smaller and/or the name of the product bigger. Perhaps we can even redesign Lumora and remove the leaf as I don't really care for what I see yet.So good luck and thanks Added Friday, August 19, 2016

I am still looking for that clean - elegant design for our product as our product is just that. If you look on the internet at vinegars and oils you will see many designs that are simple yet elegant. Creative lettering, bordering, color (can be black and white) and size will help accomplish this. So I invite you to use all your creativity and help me find just what we need.Many thanks Added Tuesday, August 23, 2016

Project Deadline Extended Reason: So many great designs coming in that I wanted a few extra days to tweek!Great job all Added Friday, August 26, 2016

Project Deadline Extended Reason: Very good designs thus far. We just need a few more days.Thanks Added Wednesday, August 31, 2016

Target Market(s)

High end grocery and specialty stores.

Our side panel on the label will say "At Lumora we're fanatics for great flavors and are passionate about finding the best ingredients. From simple to elegant our products are "simply lumora".

Industry/Entity Type

It Company

Font styles to use
Serif
Decorative
Script

Requirements
Must have
• A label that will draw the consumer to pick it up! Need something bold and elegant...
Nice to have
• Again, I really would like to have a label that pops. Since the bottle front is only about 2inches in width it will need some creativity. Would like something very simple and elegant.
• If the designer does not like the logo, please feel free to design without it!
Should not have
• Dark dark colors. We are selling dressing and we don't want any colors that may distort the contents.
• No stock photos for the front. I don't want our dressing to look like the others on the self. Brackwell Pantry just uses lettering and a their packaging is eye catching

```html
<!DOCTYPE html>
<html lang="en">
<head>
<meta charset="utf-8">
<title>Lumora Vinaigrette Labels</title>
<link rel="stylesheet" href="https://fonts.googleapis.com/css2?family=Nunito:wght@900&family=Josefin+Sans:wght@700&family=Varela+Round&display=swap">
<style>
  :root {
    --page: #ffffff;
    --ink-light: #ffffff;
    --logo-box: #2f3a21;
    --mint: #97dbb5;
    --terracotta: #bd7658;
    --olive: #a7c053;
    --index: #7dd9bf;
  }
  * { margin: 0; padding: 0; box-sizing: border-box; }
  html, body { width: 1200px; height: 1013px; overflow: hidden; background: var(--page); }
  .sheet { position: relative; width: 1200px; height: 1013px; }
  .sheet-index {
    position: absolute; left: 60px; top: 88px;
    font-family: "Varela Round", sans-serif; font-size: 44px; color: var(--index);
  }
  .label {
    position: absolute; top: 340px; width: 170px; height: 520px; overflow: hidden;
    color: var(--ink-light); text-align: center;
    font-family: "Nunito", sans-serif; font-weight: 900;
  }
  .label--mojito { left: 160px; background: var(--mint); }
  .label--sesame { left: 502px; background: var(--terracotta); }
  .label--avocado { left: 844px; background: var(--olive); }
  .brand {
    position: absolute; top: 37px; left: 50%; transform: translateX(-50%);
    background: var(--logo-box); padding: 8px 10px 6px;
    font-family: "Josefin Sans", sans-serif; font-weight: 700;
    font-size: 13px; letter-spacing: 2.5px; line-height: 1;
  }
  .flavour-note {
    position: absolute; left: 0; right: 0;
    font-size: 40px; line-height: 1; letter-spacing: 2px; white-space: nowrap;
  }
  .flavour-name { position: absolute; left: 0; right: 0; font-weight: 900; }
  .flavour-name span {
    display: block; white-space: nowrap; line-height: 1;
    font-size: 86px; letter-spacing: 2px; height: 88px;
    transform: scaleY(1.2); transform-origin: top center;
  }
  .label--mojito .flavour-note { top: 87px; }
  .label--mojito .flavour-name { top: 135px; }
  .label--sesame .flavour-note { top: 85px; font-size: 42px; letter-spacing: 1px; }
  .label--sesame .flavour-name { top: 144px; }
  .label--sesame .flavour-name span { height: 89px; }
  .label--avocado .flavour-note--top { top: 92px; font-size: 37px; letter-spacing: 0; }
  .label--avocado .flavour-name { top: 130px; }
  .label--avocado .flavour-name span {
    font-size: 92px; height: 120px; letter-spacing: 8px; transform: scaleY(1.45);
  }
  .label--avocado .flavour-note--bottom { top: 378px; font-size: 31px; letter-spacing: 1px; }
  .style-band {
    position: absolute; left: 22px; right: 22px; top: 438px;
    border-top: 2px solid var(--ink-light);
  }
  .style-name {
    display: block; padding: 7px 0 5px;
    border-bottom: 2px solid var(--ink-light);
    font-size: 21px; line-height: 22px; white-space: nowrap;
  }
  .volume {
    display: block; padding: 7px 0 6px;
    border-bottom: 2px solid var(--ink-light);
    font-size: 12px; line-height: 12px;
  }
</style>
</head>
<body>
<main class="sheet">
  <div class="sheet-index">3.</div>

  <section class="label label--mojito">
    <div class="brand">LUMORA</div>
    <div class="flavour-note">LIME</div>
    <h2 class="flavour-name"><span>MO</span><span>JI</span><span>TO</span></h2>
    <div class="style-band"><span class="style-name">VINAIGRETTE</span><span class="volume">250ml</span></div>
  </section>

  <section class="label label--sesame">
    <div class="brand">LUMORA</div>
    <div class="flavour-note">ASIAN</div>
    <h2 class="flavour-name"><span>SE</span><span>SA</span><span>ME</span></h2>
    <div class="style-band"><span class="style-name">VINAIGRETTE</span><span class="volume">250ml</span></div>
  </section>

  <section class="label label--avocado">
    <div class="brand">LUMORA</div>
    <div class="flavour-note flavour-note--top">CREAMY</div>
    <h2 class="flavour-name"><span>LI</span><span>ME</span></h2>
    <div class="flavour-note flavour-note--bottom">AVOCADO</div>
    <div class="style-band"><span class="style-name">VINAIGRETTE</span><span class="volume">250ml</span></div>
  </section>
</main>
</body>
</html>
```